Bright Harbor Crew, and interior design project management company!

We invite you to participate in our logo and web design contest for "Bright Harbor Crew Management Corp."!

Here's a brief description of our company paraphrased by ChatGPT.

Company Overview:
Bright Harbor Crew Management Corp. is your trusted partner for interior design project management, guided by international standards set forth by the Worksite Planning Guild (WPG) and the Canon of Build Practice Standards (CBPS). With a commitment to excellence, we seamlessly merge modern project management techniques with traditional values, emphasizing quality and attention to detail in every project.

Our Unique Strengths:

Local Fabrication Facility: What sets us apart is our in-house fabrication facility, a millwork shop with an impressive 20 years of experience. This facility empowers us to exercise meticulous control over the production process, ensuring that your project is crafted with precision and care right in our local community.

Experienced Skilled Workers: At Bright Harbor Crew Management Corp., our team comprises highly skilled and experienced craftsmen and artisans. They bring years of expertise to every project, guaranteeing that your interior design visions are brought to life with unmatched skill and finesse.

Serving Commercial and Residential Clients:
Our primary focus is on serving commercial clients, specializing in Tenant Improvement (TI) projects. We understand the unique demands of commercial spaces, and our project management expertise ensures that your commercial interior design projects are executed efficiently and within budget.

In addition to our commercial expertise, we also cater to discerning residential clients who seek that extra level of attention to detail. Our comprehensive services encompass all types of projects, from commercial tenant improvements to residential renovations. Regardless of the project's scale or scope, you can trust that all aspects will be managed seamlessly by our professional team.

Why Choose Us:
We are not just project managers; we are passionate advocates for your project's success. By adhering to WPG and CBPS standards, we deliver project management that is structured, efficient, and dependable. Our commitment to personal and approachable service, combined with our dedication to quality craftsmanship, ensures that your interior design projects are executed flawlessly from start to finish.

With Bright Harbor Crew Management Corp., you can trust that your project will benefit from the perfect blend of modern project management techniques and traditional values, resulting in interiors that are not only aesthetically pleasing but also built to stand the test of time.

Whether you require a commercial TI project or a residential project with meticulous attention to detail, we are the one-stop professional company that can bring your vision to life. Join our logo design contest, and let's together represent our dedication to excellence in project management and craftsmanship for both commercial and residential clients.

interior designers and architects, business owners

construction, project management, interior design, custom millwork and cabinets

1 page

• General consideration for design to float from social media to website.
• Consideration for more sophisticated backend support for customer support and project management update integrations apps such as ClickUp. (Technical portion not part of scope of work.)

```html
<!DOCTYPE html>
<html lang="en">
<head>
<meta charset="utf-8">
<title>Bright Harbor Crew Management Corp.</title>
<link href="https://fonts.googleapis.com/css2?family=Poppins:wght@300;400;500;600;700&display=swap" rel="stylesheet">
<style>
:root{
  --accent:#c49a6c;
  --accent-dark:#a97f52;
  --ink:#1b1b1b;
  --text:#555;
  --soft:#f6f6f6;
  --beige:#eee3d7;
  --footer:#111;
  --white:#fff;
}
*{box-sizing:border-box;margin:0;padding:0}
html,body{width:1200px;height:4320px;overflow:hidden}
body{font-family:'Poppins',sans-serif;color:var(--ink);background:var(--white);position:relative}
.abs{position:absolute}
section,header,footer{position:absolute;left:0;width:1200px;overflow:hidden}
.btn{position:absolute;background:var(--accent);color:var(--white);font-size:14px;font-weight:500;text-transform:uppercase;display:flex;align-items:center;justify-content:center;letter-spacing:.2px;white-space:nowrap}
.btn-frame{position:absolute;border:2px solid var(--accent)}
.photo{position:absolute}
.ghost{position:absolute;font-weight:700;color:transparent;-webkit-text-stroke:1px rgba(0,0,0,.05);text-transform:uppercase;white-space:nowrap;line-height:1}
.mark{position:absolute;width:30px;height:30px;border:2px solid var(--accent);border-radius:50%}
.sec-title{position:absolute;left:0;width:1200px;text-align:center;font-size:40px;font-weight:600;text-transform:uppercase;line-height:1}

/* header */
.site-header{top:0;height:67px;background:var(--white);border-top:3px solid var(--accent);box-shadow:0 1px 4px rgba(0,0,0,.08);z-index:5}
.brand{left:100px;top:14px;display:flex;align-items:center;gap:10px}
.brand-square{width:34px;height:34px;background:var(--accent)}
.brand-name{font-size:19px;font-weight:700;line-height:1;color:var(--ink);white-space:nowrap}
.brand-sub{font-size:8px;font-weight:600;letter-spacing:1px;margin-top:3px;color:var(--ink);white-space:nowrap}
.nav{left:358px;top:0;height:64px;display:flex;align-items:center;gap:30px;font-size:14px;font-weight:500;white-space:nowrap}
.nav .home{width:14px;height:14px}
.nav-phone{display:flex;align-items:center;gap:8px}
.phone-dot{width:26px;height:26px;border-radius:50%;background:var(--accent);display:flex;align-items:center;justify-content:center}

/* hero */
.hero{top:67px;height:623px}
.hero .photo{inset:0;background:radial-gradient(ellipse at 60% 40%,#5a4433 0%,#2e231b 50%,#161210 100%)}
.hero-title{position:absolute;left:0;width:1200px;top:225px;text-align:center;color:var(--white);font-size:45px;font-weight:600;line-height:48px;text-transform:uppercase}
.dots{position:absolute;left:1140px;top:260px;display:flex;flex-direction:column;align-items:center;gap:10px}
.dots .bar{width:6px;height:36px;border-radius:3px;background:var(--white)}
.dots .dot{width:11px;height:11px;border-radius:50%;border:1.5px solid var(--white)}

/* about */
.about{top:690px;height:592px;background:var(--soft)}
.about-text{left:655px;width:450px}
.about h2{font-size:32px;font-weight:600;line-height:37px;text-transform:uppercase;white-space:nowrap}
.about p{font-size:14px;line-height:25px;color:var(--text);text-align:justify;margin-bottom:12px}

/* services */
.services{top:1282px;height:704px;background:var(--white)}
.card{position:absolute;top:171px;width:312px;height:377px;background:var(--white);box-shadow:0 2px 8px rgba(0,0,0,.12);text-align:center}
.card .photo{left:0;top:0;width:312px;height:212px}
.card h3{position:absolute;top:228px;width:100%;font-size:21px;font-weight:500;text-transform:uppercase;white-space:nowrap}
.card p{position:absolute;top:265px;left:12px;right:12px;font-size:12.5px;line-height:23px;color:var(--text)}
.card .more{position:absolute;top:337px;width:100%;font-size:13.5px;font-weight:500;color:var(--accent);text-decoration:underline}

/* cta */
.cta{top:1986px;height:444px}
.cta .photo{inset:0;background:linear-gradient(120deg,#1e2226 0%,#3a3029 45%,#4a3a2c 70%,#241d18 100%)}
.cta h2{position:absolute;left:0;width:1200px;top:120px;text-align:center;color:var(--white);font-size:38px;font-weight:600;text-transform:uppercase}
.cta p{position:absolute;left:180px;width:840px;top:180px;text-align:center;color:#eee;font-size:17px;line-height:34px;font-weight:300}

/* portfolio */
.portfolio{top:2430px;height:872px;background:var(--white)}

/* news */
.news{top:3302px;height:653px;background:var(--soft)}
.news h4{font-size:18px;font-weight:600;line-height:20px;white-space:nowrap}
.news p{font-size:12.5px;line-height:23px;color:var(--text);text-align:justify}
.news-item{position:absolute;left:821px;width:279px}

/* footer */
.site-footer{top:3955px;height:365px;background:var(--footer);color:var(--white)}
.site-footer h5{font-size:17px;font-weight:500;text-transform:uppercase;margin-bottom:12px;white-space:nowrap}
.site-footer .small{font-size:13px;line-height:19px}
.social{position:absolute;top:4126px;width:34px;height:34px;border:1.5px solid var(--white);border-radius:50%}
.links li{list-style:none;font-size:13px;line-height:24px}
</style>
</head>
<body>

<header class="site-header">
  <div class="abs brand">
    <div class="brand-square"></div>
    <div><div class="brand-name">BRIGHT HARBOR</div><div class="brand-sub">CREW MANAGEMENT CORP</div></div>
  </div>
  <nav class="abs nav">
    <svg class="home" viewBox="0 0 14 14"><path d="M7 1 1 7h2v6h3V9h2v4h3V7h2z" fill="#c49a6c"/></svg>
    <span>ABOUT</span><span>SERVICES</span><span>PORTFOLIO</span><span>BLOG</span><span>CONTACT US</span>
    <span class="nav-phone"><span class="phone-dot"><svg width="12" height="12" viewBox="0 0 12 12"><path d="M2.5 1 4.5 3.3 3.6 4.7c.7 1.5 2 2.8 3.7 3.7l1.4-.9L11 9.5 9.8 11C5.5 10.6 1.4 6.5 1 2.2z" fill="#fff"/></svg></span>+1 555-014-2290 <span style="color:#aaa">|</span> ◍ EN ⌄</span>
  </nav>
</header>

<section class="hero">
  <div class="photo" role="img" aria-label="Dark modern living room with wood floor and lounge seating"></div>
  <h1 class="hero-title">Bright Harbor Crew<br>Management Corp</h1>
  <div class="btn" style="left:483px;top:348px;width:233px;height:38px">Start your project now</div>
  <div class="dots"><div class="bar"></div><div class="dot"></div><div class="dot"></div><div class="dot"></div></div>
</section>

<section class="about">
  <div class="abs" style="left:318px;top:70px;width:274px;height:420px;background:var(--beige)"></div>
  <div class="photo" role="img" aria-label="Living room with fireplace, shelves and armchairs" style="left:119px;top:88px;width:456px;height:414px;background:linear-gradient(160deg,#8a8f95,#5e6064 55%,#8e7b66)"></div>
  <div class="abs" style="left:100px;top:228px;width:4px;height:292px;background:var(--ink)"></div>
  <div class="abs" style="left:100px;top:516px;width:312px;height:4px;background:var(--ink)"></div>
  <div class="ghost" style="left:770px;top:45px;font-size:110px">About</div>
  <div class="mark" style="left:655px;top:110px"></div>
  <div class="abs about-text" style="top:163px">
    <h2>About Bright Harbor<br>Crew Management Corp</h2>
  </div>
  <div class="abs" style="left:1040px;top:181px;width:50px;height:1.5px;background:var(--accent)"></div>
  <div class="abs" style="left:1088px;top:177px;width:9px;height:9px;border-radius:50%;background:var(--accent)"></div>
  <div class="abs about-text" style="top:243px">
    <p>Sed ut perspiciatis unde omnis iste natus error sit voluptatem accusantium doloremque laudantium, totam rem aperiam, eaque ipsa quae ab illo inventore veritatis et quasi architecto beatae vitae dicta sunt explicabo.</p>
    <p>Sed ut perspiciatis unde omnis iste natus error sit voluptatem accusantium doloremque laudantium</p>
  </div>
  <div class="btn-frame" style="left:650px;top:444px;width:180px;height:42px"></div>
  <div class="btn" style="left:655px;top:436px;width:180px;height:42px">Learn more about</div>
</section>

<section class="services">
  <div class="ghost" style="left:0;width:1200px;text-align:center;top:35px;font-size:100px">Services</div>
  <div class="mark" style="left:585px;top:50px"></div>
  <h2 class="sec-title" style="top:103px">What we offer</h2>
  <div class="card" style="left:100px">
    <div class="photo" role="img" aria-label="Bright lounge with pale armchairs and floor lamp" style="background:linear-gradient(135deg,#d9d3c9,#a9b2b3)"></div>
    <h3>Architectural Design</h3>
    <p>Lorem ipsum dolor sit ametectetur adipiscing elit, sed do eiusmod tempor incididunt ut labore et dolore magna aliqua.</p>
    <div class="more">LEARN MORE</div>
  </div>
  <div class="card" style="left:444px">
    <div class="photo" role="img" aria-label="White living room with coffered ceiling" style="background:linear-gradient(135deg,#e4e2de,#b7b2aa)"></div>
    <h3>Interior Design</h3>
    <p>Lorem ipsum dolor sit ametectetur adipiscing elit, sed do eiusmod tempor incididunt ut labore et dolore magna aliqua.</p>
    <div class="more">LEARN MORE</div>
  </div>
  <div class="card" style="left:788px">
    <div class="photo" role="img" aria-label="Dark sofa with cushions under framed art" style="background:linear-gradient(135deg,#5a5048,#2f2925)"></div>
    <h3>Furnishing Services</h3>
    <p>Lorem ipsum dolor sit ametectetur adipiscing elit, sed do eiusmod tempor incididunt ut labore et dolore magna aliqua.</p>
    <div class="more">LEARN MORE</div>
  </div>
  <div class="btn-frame" style="left:505px;top:590px;width:182px;height:42px"></div>
  <div class="btn" style="left:512px;top:582px;width:180px;height:42px">View all services</div>
</section>

<section class="cta">
  <div class="photo" role="img" aria-label="Dim living room with sofa and warm lamp light"></div>
  <h2>Want you decorate your interior?</h2>
  <p>Sed ut perspiciatis unde omnis iste natus sit voluptatem accusantium doloque laudantium, totam rem aperiam, eaque ipsa quae ab illo inventore veritatis et quasi</p>
  <div class="btn-frame" style="left:505px;top:280px;width:182px;height:40px"></div>
  <div class="btn" style="left:510px;top:273px;width:180px;height:40px">Contact us</div>
</section>

<section class="portfolio">
  <div class="ghost" style="left:0;width:1200px;text-align:center;top:90px;font-size:100px">Portfolio</div>
  <div class="mark" style="left:585px;top:100px"></div>
  <h2 class="sec-title" style="top:133px">Our portfolio</h2>
  <div class="photo" role="img" aria-label="Open living room with leather sofa" style="left:114px;top:198px;width:312px;height:213px;background:linear-gradient(135deg,#ebe7e1,#b58c6a)"></div>
  <div class="photo" role="img" aria-label="Room with yellow armchair and floor lamp" style="left:114px;top:433px;width:312px;height:276px;background:linear-gradient(135deg,#e2e0dc,#cdb46a)"></div>
  <div class="photo" role="img" aria-label="Wooden staircase with pendant lights" style="left:444px;top:198px;width:312px;height:278px;background:linear-gradient(160deg,#f0eeea,#c9a47a)"></div>
  <div class="photo" role="img" aria-label="Dining room facing the sea at dusk" style="left:444px;top:496px;width:312px;height:213px;background:linear-gradient(180deg,#4e5460,#a07a62)"></div>
  <div class="photo" role="img" aria-label="Bright lounge with pale armchairs" style="left:774px;top:198px;width:312px;height:213px;background:linear-gradient(135deg,#d9d3c9,#a9b2b3)"></div>
  <div class="photo" role="img" aria-label="Sage wall with round mirror, console and plants" style="left:774px;top:433px;width:312px;height:276px;background:linear-gradient(160deg,#b9bca5,#c9a583)"></div>
  <div class="btn-frame" style="left:505px;top:749px;width:182px;height:40px"></div>
  <div class="btn" style="left:510px;top:742px;width:180px;height:40px">View all</div>
</section>

<section class="news">
  <div class="ghost" style="left:0;top:50px;font-size:100px">Blogs</div>
  <div class="mark" style="left:583px;top:82px"></div>
  <h2 class="sec-title" style="top:120px">Our latest news</h2>
  <div class="photo" role="img" aria-label="Dark bedroom with upholstered bed and brass chandelier" style="left:100px;top:192px;width:467px;height:378px;background:linear-gradient(150deg,#3a3734,#6e6760 60%,#d8d2ca)"></div>
  <div class="abs" style="left:144px;top:456px;width:443px;height:136px;background:var(--white);border:1px solid #e3d6c8;padding:18px 20px 0 20px">
    <div style="width:276px"><h4 style="font-size:17px">Finibus Bonorum et Malorum<br>written by Aurelio in 45 BC</h4>
    <p style="margin-top:4px">Lorem ipsum dolor sit ametectetur adipiscing elit, sed do eiusmod tempor incididunt ut labore et</p></div>
  </div>
  <div class="btn-frame" style="left:446px;top:514px;width:126px;height:40px"></div>
  <div class="btn" style="left:451px;top:506px;width:124px;height:40px;font-size:13px">Learn more</div>

  <div class="photo" role="img" aria-label="Grey sofa with wooden side tables" style="left:622px;top:192px;width:181px;height:177px;background:linear-gradient(150deg,#e1ded9,#a38062)"></div>
  <div class="news-item" style="top:200px">
    <h4>Finibus Bonorum et Malorum<br>written by Aurelio in 45 BC</h4>
    <p style="margin-top:2px">Lorem ipsum dolor sit ametectetur adipiscing elit, sed do eiusmod tempor incididunt ut labore et dolore magna aliqua.</p>
  </div>
  <div class="btn-frame" style="left:821px;top:342px;width:120px;height:38px"></div>
  <div class="btn" style="left:826px;top:334px;width:120px;height:38px;font-size:13px">Learn more</div>
  <div class="abs" style="left:622px;top:390px;width:478px;height:1px;background:#ddd"></div>

  <div class="photo" role="img" aria-label="Dining room with wooden table and orange pendant" style="left:622px;top:410px;width:181px;height:176px;background:linear-gradient(150deg,#cfc6b8,#8b5b34)"></div>
  <div class="news-item" style="top:418px">
    <h4>Finibus Bonorum et Malorum<br>written by Aurelio in 45 BC</h4>
    <p style="margin-top:2px">Lorem ipsum dolor sit ametectetur adipiscing elit, sed do eiusmod tempor incididunt ut labore et dolore magna aliqua.</p>
  </div>
  <div class="btn-frame" style="left:821px;top:560px;width:120px;height:38px"></div>
  <div class="btn" style="left:826px;top:552px;width:120px;height:38px;font-size:13px">Learn more</div>
</section>

<footer class="site-footer">
  <div class="abs brand" style="top:86px">
    <div class="brand-square"></div>
    <div><div class="brand-name" style="color:#fff">BRIGHT HARBOR</div><div class="brand-sub" style="color:#fff">CREW MANAGEMENT CORP</div></div>
  </div>
  <div class="abs" style="left:402px;top:84px;width:210px">
    <h5>Contact us</h5>
    <p class="small">⌖ 48 Harbor Lane<br>Eastport, US 20417</p>
    <p class="small" style="margin-top:14px">✆ +1 555-014-2290</p>
    <p class="small" style="margin-top:18px;white-space:nowrap">✉ info@brightharbor.example</p>
  </div>
  <div class="abs" style="left:630px;top:84px">
    <h5>Quick links</h5>
    <ul class="links"><li>Home</li><li>About</li><li>Services</li><li>Portfolio</li><li>News</li><li>Careers</li><li>Contact</li></ul>
  </div>
  <div class="abs" style="left:803px;top:84px;width:297px">
    <h5>Sign for newslatter</h5>
    <p class="small">Stay connected on new products, events and offers. Valid for new email subscribers only.</p>
  </div>
  <div class="abs" style="left:803px;top:168px;width:297px;height:36px;border:1px solid #555;display:flex;align-items:center;padding-left:14px;font-size:13px">Eamil</div>
  <div class="abs" style="left:1058px;top:169px;width:41px;height:34px;background:var(--accent);display:flex;align-items:center;justify-content:center">
    <svg width="14" height="14" viewBox="0 0 14 14"><path d="M1 7 13 1 9 13 7 8z" fill="#fff"/></svg>
  </div>
  <div class="abs" style="left:100px;top:297px;width:1000px;height:1px;background:#444"></div>
  <div class="abs" style="left:0;width:1200px;top:316px;text-align:center;font-size:13px">Copyright ©2023 BRIGHT HARBOR CREW MANAGEMENT CORP. All Rights Reserved.</div>
</footer>
<div class="social" style="left:139px"></div>
<div class="social" style="left:182px"></div>
<div class="social" style="left:226px"></div>
<div class="social" style="left:270px"></div>

</body>
</html>
```